Business Card & Stationery for Orin Basket
Video Production
Business Card & Stationery for Orin Basket - Video
Creative Brief
Professional
Marlo-Tav Endu
info@orinbasket.com
www.orinbasket.com
Concepts
BUSINESS CARD, LETTERHEAD ENVELOPES FOR VIDEO PRODUCTION COMPANY

```html
<!DOCTYPE html>
<html lang="en">
<head>
<meta charset="utf-8">
<title>Orin Basket — Stationery Concepts</title>
<link href="https://fonts.googleapis.com/css2?family=Montserrat:wght@300;400;600&family=Open+Sans:wght@400;600&display=swap" rel="stylesheet">
<style>
:root{
  --bg:#e9e6e1;
  --ink:#161616;
  --ink-soft:#2c2c2c;
  --paper:#ffffff;
  --grey:#9a9a9a;
  --grey-light:#d6d6d6;
  --text:#555;
  --accent:#cfcfcf;
}
*{margin:0;padding:0;box-sizing:border-box}
html,body{width:1200px;height:272px;overflow:hidden;background:var(--bg)}
body{position:relative;font-family:"Open Sans",sans-serif;color:var(--text)}
.piece{position:absolute;box-shadow:0 2px 6px rgba(0,0,0,.25)}
.brand{font-family:"Montserrat",sans-serif;font-weight:300;letter-spacing:.18em;text-transform:uppercase;color:var(--paper);white-space:nowrap;display:flex;align-items:center;gap:4px}
.brand .dot{width:6px;height:6px;border-radius:50%;background:var(--accent)}
.brand.dark{color:var(--ink)}
.brand.dark .dot{background:var(--ink)}
.concept-label{position:absolute;left:12px;top:140px;font-size:8px;color:var(--ink-soft);font-family:"Montserrat",sans-serif}

/* business cards */
.card{background:var(--ink);display:flex;align-items:center;justify-content:center}
.card-front{left:12px;top:72px;width:108px;height:56px}
.card-back{left:12px;top:196px;width:108px;height:56px;flex-direction:column;align-items:flex-start;padding:8px 10px;justify-content:space-between}
.card-back .who{font-size:5px;color:var(--grey-light);line-height:1.4}
.card-back .who b{display:block;font-size:6px;color:var(--paper);font-weight:600}

/* letterheads */
.letterhead{background:var(--paper);width:138px;height:216px;top:36px;padding:0 10px;font-size:4px;line-height:1.6}
.letterhead .head{height:22px;margin:0 -10px 10px;background:var(--ink);display:flex;align-items:center;justify-content:flex-end;padding-right:8px}
.letterhead .head .brand{font-size:5px}
.letterhead p{margin-bottom:4px}
.letterhead .sign{margin-top:14px;font-weight:600;color:var(--ink-soft)}
.letterhead .foot{position:absolute;left:10px;right:10px;bottom:8px;border-top:1px solid var(--grey-light);padding-top:3px;font-size:3.6px;color:var(--grey)}
.lh-1{left:149px}
.lh-2{left:312px}

/* compliment slip and small card */
.slip{left:492px;top:108px;width:130px;height:42px;background:var(--ink);display:flex;align-items:center;justify-content:center}
.slip .brand{font-size:7px}
.mini-card{left:630px;top:112px;width:66px;height:36px;background:var(--paper);border-top:12px solid var(--ink)}

/* envelopes */
.envelope{background:var(--paper);overflow:hidden}
.envelope .band{height:12px;background:var(--ink);display:flex;align-items:center;padding-left:8px}
.envelope .band .brand{font-size:4.5px}
.env-1{left:492px;top:168px;width:208px;height:36px}
.env-2{left:492px;top:216px;width:208px;height:36px}
.env-2 .band{margin-top:24px}
.env-flap{left:720px;top:36px;width:204px;height:84px;background:linear-gradient(180deg,#f4f4f4,var(--grey-light))}
.env-black{left:720px;top:132px;width:204px;height:48px;background:var(--ink);display:flex;align-items:center;justify-content:center}
.env-black .brand{font-size:7px}
.env-white{left:720px;top:192px;width:204px;height:48px}
.env-white .band{height:14px}

/* presentation folder */
.folder{left:953px;top:36px;width:240px;height:216px;background:radial-gradient(circle at 35% 40%,#5a5a5a 0%,#2a2a2a 55%,var(--ink) 100%)}
.folder .cover{position:absolute;left:0;top:0;width:120px;height:216px;display:flex;align-items:center;justify-content:center;border-right:1px solid #111}
.folder .cover .brand{font-size:7px}
.folder svg{position:absolute;right:0;bottom:0}
.folder .card-in{position:absolute;right:22px;bottom:24px;width:48px;height:26px;background:var(--ink);border:1px solid #444;display:flex;align-items:center;justify-content:center}
.folder .card-in .brand{font-size:3.5px}
</style>
</head>
<body>

<div class="concept-label">Stationery Concepts</div>

<div class="piece card card-front"><span class="brand" style="font-size:8px"><span class="dot"></span>Orin Basket</span></div>
<div class="piece card card-back">
  <span class="brand" style="font-size:6px"><span class="dot"></span>Orin Basket</span>
  <div class="who"><b>Marlo-Tav Endu</b>Creative Director<br>info@orinbasket.com<br>www.orinbasket.com</div>
</div>

<article class="piece letterhead lh-1">
  <div class="head"><span class="brand"><span class="dot"></span>Orin Basket</span></div>
  <p>Dear Client,</p>
  <p>Thank you for your interest in our video work.</p>
  <p>Our team plans, shoots and edits every story with care.</p>
  <p>We look forward to starting your next project soon.</p>
  <p>Kind regards,</p>
  <p class="sign">Marlo-Tav Endu</p>
  <div class="foot">info@orinbasket.com &nbsp;|&nbsp; www.orinbasket.com</div>
</article>

<article class="piece letterhead lh-2">
  <div class="head"><span class="brand"><span class="dot"></span>Orin Basket</span></div>
  <p>Dear Client,</p>
  <p>Thank you for your interest in our video work.</p>
  <p>Our team plans, shoots and edits every story with care.</p>
  <p>We look forward to starting your next project soon.</p>
  <p>Kind regards,</p>
  <p class="sign">Marlo-Tav Endu</p>
  <div class="foot">info@orinbasket.com &nbsp;|&nbsp; www.orinbasket.com</div>
</article>

<div class="piece slip"><span class="brand"><span class="dot"></span>Orin Basket</span></div>
<div class="piece mini-card"></div>

<div class="piece envelope env-1"><div class="band"><span class="brand"><span class="dot"></span>Orin Basket</span></div></div>
<div class="piece envelope env-2"><div class="band"><span class="brand"><span class="dot"></span>Orin Basket</span></div></div>

<div class="piece env-flap"></div>
<div class="piece env-black"><span class="brand"><span class="dot"></span>Orin Basket</span></div>
<div class="piece envelope env-white"><div class="band"><span class="brand"><span class="dot"></span>Orin Basket</span></div></div>

<div class="piece folder">
  <div class="cover"><span class="brand"><span class="dot"></span>Orin Basket</span></div>
  <svg width="120" height="90" viewBox="0 0 120 90"><path d="M0 30 Q60 0 120 20 L120 90 L0 90 Z" fill="#1e1e1e" stroke="#3a3a3a"/></svg>
  <div class="card-in"><span class="brand">Orin Basket</span></div>
</div>

</body>
</html>
```